Government contracting small business needs a web design

Tarrow Ridge Inc is a veteran owned small business that delivers a full range of professional services as well as training in information technology, security and defense intelligence solutions.
We need a professional/corporate looking website where potential clients can view what services are offered.
This being a new company, there is not much that can added more than a narrative statement, stock photos and a place where potential customers and employees can make contact.
Open to ideas.
Target Market(s)
US Government
Industry/Entity Type
Small Business

```html
<!DOCTYPE html>
<html lang="en">
<head>
<meta charset="utf-8">
<title>Tarrow Ridge – IT security and intelligence solutions</title>
<link rel="stylesheet" href="https://fonts.googleapis.com/css2?family=Arimo:wght@400;700&display=swap">
<style>
:root{
  --backdrop:#3b4045;
  --page:#ffffff;
  --ink:#222222;
  --body-ink:#333333;
  --teal:#3d9aa8;
  --orange:#f7a21b;
  --nav-top:#3c3c3c;
  --nav-bottom:#0d0d0d;
  --cyan:#2fa6d8;
  --footer:#111111;
  --gold:#c9b54a;
  --muted:#9a9a9a;
}
*{margin:0;padding:0;box-sizing:border-box}
html,body{width:837px;height:1200px;overflow:hidden}
body{background:var(--backdrop);font-family:"Arimo",Arial,sans-serif;color:var(--ink);position:relative}
.abs{position:absolute}
.page{position:absolute;left:25px;top:3px;width:773px;height:1010px;background:var(--page)}
.ph{position:absolute}

/* header */
.brand{left:32px;top:20px;display:flex;align-items:center;gap:6px}
.brand-dot{width:44px;height:44px;border-radius:50%;background:#7a7a7a}
.brand-name{font-size:29px;font-weight:700;color:#3a3a3a;letter-spacing:-.3px}
.header-photo{left:470px;top:0;width:303px;height:74px;background:linear-gradient(90deg,#ffffff 0%,#9fb3cc 18%,#3e6796 40%,#29507f 60%,#8aa0bb 78%,#d6d9de 100%)}
.top-links{left:523px;top:1px;width:145px;height:24px;background:#fff;font-size:10px;color:#333;display:flex;align-items:center;justify-content:center}

/* navigation */
.nav{left:0;top:74px;width:773px;height:27px;background:linear-gradient(var(--nav-top),var(--nav-bottom));display:flex}
.nav a{color:#fff;text-decoration:none;font-size:11px;padding:0 8px;line-height:27px;border-right:1px solid #888}
.nav a.active{background:var(--orange);width:53px;text-align:center}
.nav .contact{margin-left:auto;color:var(--cyan);font-weight:700;font-size:10px;line-height:27px;padding-right:25px;word-spacing:3px}

/* hero */
.hero{left:0;top:101px;width:773px;height:230px;background:linear-gradient(100deg,#e4e8ec 0%,#b7c0cc 12%,#4a5566 26%,#7e889a 38%,#c9cddc 55%,#b4b8cf 75%,#a6aac2 100%)}
.hero-band{left:0;top:331px;width:773px;height:38px;background:linear-gradient(#9a9eb3,#8e92a8)}
.hero-caption{left:304px;top:257px;width:449px;height:59px;background:#000;border-radius:4px;color:#fff;font-size:26px;display:flex;align-items:center;justify-content:center}
.dots{left:20px;top:345px;display:flex;gap:3px}
.dots span{width:9px;height:9px;border-radius:50%;background:#fff}
.dots span:first-child{border:1px solid #555}

/* services */
.section-title{left:32px;top:387px;font-size:19px;font-weight:400;color:#111}
.service-title{font-size:14px;font-weight:400;color:var(--teal)}
.service-text{font-size:8.4px;line-height:9.2px;color:var(--body-ink)}

/* bottom row */
.promo{height:44px;border:1px solid #bbb;border-radius:3px;background:linear-gradient(#fff,#e8e8e8);font-size:10px}
.promo .thumb{position:absolute;left:3px;top:3px;width:40px;height:38px;background:linear-gradient(#c8c8c8,#6f6f6f)}
.promo .l1{position:absolute;left:46px;top:4px}
.promo .l2{position:absolute;left:46px;top:17px;font-size:11px}
.promo .l3{position:absolute;right:4px;bottom:2px;font-size:8px}
.jobs{left:336px;top:962px;width:103px;height:24px;background:linear-gradient(#f3f3f3,#dcdcdc);font-size:11px;display:flex;align-items:center;gap:6px;padding-left:6px}
.jobs i{width:16px;height:12px;background:#7b7b7b;border-radius:2px}
.badge-blue{left:476px;top:942px;width:78px;height:47px;background:linear-gradient(135deg,#1f72c6,#5fb4ee)}
.badge-round{left:626px;top:947px;width:44px;height:44px;border-radius:50%;background:#3b8fc9}

/* footer */
.footer-band{left:0;top:1013px;width:837px;height:187px;background:var(--footer)}
.footer-mark{left:53px;top:1030px;width:97px;height:97px;border-radius:50%;background:radial-gradient(circle at 40% 35%,#f2c23b,#c58f0c)}
.footer-name{left:40px;top:1137px;width:122px;height:28px;background:#fff;color:#000;font-size:14px;font-weight:700;display:flex;align-items:center;justify-content:center}
.address{left:181px;top:1040px;font-size:10px;line-height:10.8px;color:var(--gold);font-style:normal}
.phone{left:180px;top:1099px;font-size:11px;line-height:18px;color:var(--muted)}
.copy{left:380px;top:1101px;font-size:9px;color:#ddd}
.legal{left:665px;top:1101px;font-size:9px;color:#ddd}
.rule{left:353px;top:1125px;width:445px;height:1px;background:#333}
.follow{left:482px;top:1144px;font-size:8px;color:#444}
.social{left:605px;top:1138px;display:flex;gap:10px}
.social span{width:22px;height:22px;border-radius:3px}
</style>
</head>
<body>
<div class="page">
  <div class="ph header-photo" role="img" aria-label="Photo of business people looking up beside glowing data screens"></div>
  <div class="ph brand"><span class="brand-dot"></span><span class="brand-name">Tarrow Ridge</span></div>
  <div class="ph top-links">Carrers | Location | Contact us</div>

  <nav class="ph nav">
    <a class="active" href="#">Home</a>
    <a href="#">Company</a>
    <a href="#">Industry we Serve</a>
    <a href="#">Services</a>
    <a href="#">Solution we provide</a>
    <span class="contact">Phone : 12345678 &nbsp; Fax : 12345678</span>
  </nav>

  <div class="ph hero" role="img" aria-label="Photo of three colleagues working together at a laptop in a bright glass office"></div>
  <div class="ph hero-band"></div>
  <div class="ph hero-caption">IT security and intelligence solutions</div>
  <div class="ph dots"><span></span><span></span><span></span></div>

  <h1 class="ph section-title">IT security and Intelligence Solutions</h1>

  <h2 class="ph service-title" style="left:35px;top:420px">Recruitment Services</h2>
  <div class="ph" role="img" aria-label="Photo of an interview meeting around an office table" style="left:35px;top:447px;width:166px;height:110px;background:linear-gradient(135deg,#e6eaee 0%,#b9c3cc 45%,#5d6670 75%,#9aa3ab 100%)"></div>
  <p class="ph service-text" style="left:33px;top:565px;width:222px">The recruitment and selection is the major function of the human resource department and recruitment process is the first step towards creating the competitive strength and the strategic advantage for the organisations. Recruitment process involves a systematic procedure from sourcing the candidates to arranging and conducting the interviews and requires many resources and time.</p>

  <h2 class="ph service-title" style="left:410px;top:420px">IT SECURITY</h2>
  <div class="ph" role="img" aria-label="Photo of a man drawing a network security diagram on glass" style="left:385px;top:445px;width:177px;height:118px;background:linear-gradient(90deg,#fafafa 0%,#eeeeee 45%,#c9b7a6 70%,#8a8f99 100%)"></div>
  <p class="ph service-text" style="left:393px;top:572px;width:222px">Our cyber security practice protects government networks and data from evolving threats. We assess risk, harden systems, monitor activity and respond to incidents so your mission keeps running. By meeting federal compliance standards and training your staff, we help you build a stronger, more resilient security posture.</p>

  <h2 class="ph service-title" style="left:35px;top:656px">Intelligence Solutions</h2>
  <div class="ph" role="img" aria-label="Photo of a smiling woman holding a globe" style="left:35px;top:682px;width:179px;height:99px;background:linear-gradient(90deg,#efe9e3 0%,#d8cfc6 35%,#9dd6ee 65%,#6cbfe6 100%)"></div>
  <p class="ph service-text" style="left:33px;top:797px;width:222px">Wireless solutions provide full-duplex wireless connectivity at variable distances from less than 1 mile to as far as 40 miles away. They are ideal alternatives to multiple E1/T1s or fiber-optic cables and can be used to extend or provide redundancy to existing fiber networks. Because they are wireless and license-free, WANs eliminate wire/fiber installation costs and recurring monthly fees - delivering carrier-class performance quickly, at a fraction of the cost of wired connections.</p>

  <h2 class="ph service-title" style="left:410px;top:656px;word-spacing:4px">Enterprise IT Services</h2>
  <div class="ph" role="img" aria-label="Photo of a man sketching a system diagram on a board" style="left:400px;top:679px;width:167px;height:106px;background:linear-gradient(90deg,#7f8790 0%,#a9b0b8 50%,#8fb0d6 80%,#c7ccd2 100%)"></div>
  <p class="ph service-text" style="left:387px;top:797px;width:244px">Many organizations' IT strategy still remains closely focused on running existing operations. They face an array of issues that prevent them from investing in IT innovation, resulting in lower revenue growths &amp; impacting their competitiveness in today's global markets.<br><br>We enable organizations for IT innovation by streamlining their business processes and enhancing their effectiveness with accelerators. By partnering with us, our customers are fast tracked to the world of IT innovation.</p>

  <div class="ph promo" style="left:28px;top:944px;width:119px">
    <span class="thumb" role="img" aria-label="Photo of a client"></span>
    <span class="l1">Testimonials</span><span class="l2">From clients</span><span class="l3">Click here...</span>
  </div>
  <div class="ph promo" style="left:169px;top:944px;width:119px">
    <span class="thumb" role="img" aria-label="Photo of a projector"></span>
    <span class="l1">See</span><span class="l2">Our Portfolio</span><span class="l3">Click here...</span>
  </div>
  <div class="ph jobs"><i></i>Job Openings</div>
  <div class="ph badge-blue"></div>
  <div class="ph badge-round"></div>
</div>

<footer>
  <div class="abs footer-band"></div>
  <div class="abs footer-mark"></div>
  <div class="abs footer-name">Tarrow Ridge</div>
  <address class="abs address">Tarrow Ridge<br>No.4 Harwick Lane<br>Eastbury<br>Kentshire<br>KT4 2RW</address>
  <div class="abs phone">Phone : 123456789<br>Fax : 123456789</div>
  <div class="abs copy">Copyright © 2012 • TARROWRIDGE.COM• All rights reserved</div>
  <div class="abs legal">Privacy policy | Terms of Use</div>
  <div class="abs rule"></div>
  <div class="abs follow">Follow us on social network</div>
  <div class="abs social">
    <span style="background:#3b5a9a"></span>
    <span style="background:#3fb4e6"></span>
    <span style="background:#e9e9e9"></span>
    <span style="background:#1f6fae"></span>
    <span style="background:#3b5876"></span>
    <span style="background:#f28a1c"></span>
  </div>
</footer>
</body>
</html>
```